Flyer for local business that installs fences and sells fence materials

We recently began selling fence materials, in addition to also doing fence installations. We need a flyer that displays our business information and photos of our work, as well as a flyer that shows customers they have the option to buy materials only also.

If they are looking to build a fence - we can help by installing it, or if they want to install themselves, they can buy the materials only from us too. We provide a lifetime warranty on all materials and installations. More information about the company is here: www.BrambleRailWorks.com

Its important to have the company logo, phone number, email and business hours listed (Monday - Thursday 9AM - 3PM, Friday 9AM - 1PM).

It is also important to show the fence material types we offer:
Wood, Chainlink, Vinyl and Aluminum
Updates

Updated with more photos and url to website www.bramblerailworks.com for details

Target Market(s)

Residential Homeowners

Industry/Entity Type

Construction

Font styles to use
Sans Serif
Other font styles liked:
• Arial

Colors
0054AA
0677BA
7BADD7
CADEEF
E8F1F8

Requirements
Must have
• Photos of the fencing we offer
Nice to have
• A way to explain to customers they can hire us to install, or just buy the materials from us
Should not have
• Too many colors or too many words

```html
<!DOCTYPE html>
<html lang="en">
<head>
<meta charset="utf-8">
<title>Bramble Rail Works – Fence Flyer</title>
<link href="https://fonts.googleapis.com/css2?family=Montserrat:wght@400;500;600;700;800;900&display=swap" rel="stylesheet">
<style>
  :root {
    --page-bg: #e9e9e7;
    --brown: #5b3b22;
    --brown-dark: #4a2f1b;
    --orange: #ef9230;
    --blue: #2a7cc7;
    --blue-light: #3f8fd6;
    --text-dark: #3a2a1e;
    --white: #ffffff;
    --rule: #c9c9c9;
  }
  * { box-sizing: border-box; margin: 0; padding: 0; }
  html, body { width: 1200px; height: 2865px; overflow: hidden; }
  body { background: var(--page-bg); font-family: "Montserrat", Arial, sans-serif; position: relative; }

  .flyer {
    position: absolute; left: 50px; top: 720px;
    width: 806px; height: 1044px;
    background: var(--white);
    transform: scale(1.365); transform-origin: top left;
    overflow: hidden;
    box-shadow: 0 4px 18px rgba(0,0,0,.12);
  }
  .abs { position: absolute; }

  /* header */
  .brand-mark { left: 48px; top: 38px; width: 52px; height: 52px; border-radius: 50%; background: var(--orange); }
  .brand-name { left: 116px; top: 30px; font-size: 24px; font-weight: 800; color: var(--blue); letter-spacing: .2px; }
  .brand-phone { left: 116px; top: 58px; font-size: 25px; font-weight: 800; color: var(--text-dark); }
  .brand-tagline { left: 117px; top: 89px; font-size: 7.5px; font-weight: 700; color: var(--text-dark); }

  /* hero */
  .hero { left: 0; top: 117px; width: 375px; height: 406px; background: linear-gradient(160deg, #6a4529 0%, var(--brown) 45%, var(--brown-dark) 100%); }
  .hero-accent { left: 49px; top: 222px; width: 72px; height: 82px; background: var(--orange); opacity: .85; }
  .hero-title { left: 62px; top: 248px; font-size: 47px; line-height: 46px; font-weight: 800; color: var(--white); }
  .hero-sub { left: 62px; top: 354px; font-size: 21px; line-height: 23px; font-weight: 500; color: var(--white); }

  /* photos */
  .photo { background: linear-gradient(180deg, #6d8f4a 0%, #8aa25a 45%, #d8bf8a 60%, #c9a46a 100%); }
  .photo-yard { left: 385px; top: 0; width: 421px; height: 277px; background: linear-gradient(180deg, #b9c8b0 0%, #6f9a3f 30%, #7ea24e 50%, #d9c18e 62%, #c7a56b 100%); }
  .photo-install { left: 385px; top: 287px; width: 205px; height: 236px; background: linear-gradient(180deg, #dcc79a 0%, #cdb080 40%, #71923f 75%, #5f7f36 100%); }
  .photo-chainlink { left: 600px; top: 287px; width: 206px; height: 236px; background: linear-gradient(180deg, #c8cfcf 0%, #9aa58f 35%, #6e8748 70%, #5b7436 100%); }
  .photo-boards { left: 334px; top: 818px; width: 196px; height: 152px; background: linear-gradient(90deg, #c9a467 0%, #e1c690 45%, #cfae75 100%); }

  /* selling column */
  .sell-lead { left: 68px; top: 543px; font-size: 23px; line-height: 25px; font-weight: 400; color: var(--blue); }
  .sell-strong { left: 68px; top: 593px; font-size: 25.5px; line-height: 26.5px; font-weight: 800; color: var(--blue); }
  .perks { left: 68px; top: 683px; width: 227px; list-style: none; }
  .perks li { font-size: 11.5px; font-weight: 600; color: var(--text-dark); border-bottom: 1px solid var(--rule); height: 33px; padding-top: 9px; display: flex; align-items: flex-start; gap: 3px; }
  .perks li:last-child { height: 38px; padding-top: 11px; }
  .perks svg { flex: none; margin-top: 1px; }
  .perks small { display: block; font-size: 10px; font-weight: 400; color: #666; margin-left: 14px; }
  .contact-cta { left: 68px; top: 976px; font-size: 16px; font-weight: 800; color: var(--text-dark); }

  /* estimates column */
  .estimate-title { left: 334px; top: 557px; font-size: 24px; line-height: 23px; font-weight: 800; color: var(--orange); }
  .estimate-copy { left: 334px; top: 643px; width: 190px; font-size: 13.2px; line-height: 12.4px; font-weight: 500; color: var(--text-dark); }
  .estimate-note { left: 334px; top: 760px; width: 190px; font-size: 13.2px; line-height: 14px; font-weight: 600; color: var(--text-dark); }

  /* materials panel */
  .materials { left: 572px; top: 555px; width: 234px; height: 308px; background: var(--brown); }
  .materials-tab { left: 570px; top: 556px; width: 206px; height: 43px; background: var(--orange); clip-path: polygon(0 0, 100% 0, 96% 100%, 4% 100%); color: var(--white); font-size: 16.5px; line-height: 16px; font-weight: 800; text-align: center; padding-top: 5px; }
  .material { left: 548px; width: 258px; height: 54px; display: flex; align-items: center; }
  .material::after { content: ""; position: absolute; left: 50px; right: 6px; bottom: -5px; height: 1px; background: rgba(255,255,255,.5); }
  .material:last-child::after { display: none; }
  .material-icon { width: 50px; height: 50px; border-radius: 50%; background: var(--white); border: 4px solid var(--orange); display: flex; align-items: center; justify-content: center; flex: none; }
  .material-name { margin-left: 14px; font-size: 16px; font-weight: 700; color: var(--white); }

  /* steps */
  .steps-title { left: 562px; top: 870px; width: 204px; text-align: center; font-size: 17.5px; line-height: 17px; font-weight: 800; color: var(--blue); }
  .steps { left: 568px; top: 913px; list-style: none; }
  .steps li { font-size: 11px; font-weight: 600; color: var(--text-dark); height: 19.5px; display: flex; align-items: center; gap: 6px; }
  .steps b { width: 11px; height: 11px; border-radius: 50%; background: var(--text-dark); color: var(--white); font-size: 7.5px; display: inline-flex; align-items: center; justify-content: center; }

  /* footer bars */
  .footer { left: 0; top: 1012px; width: 806px; height: 32px; }
  .footer-phone { left: 68px; top: 1014px; font-size: 22px; font-weight: 800; color: var(--white); display: flex; align-items: center; gap: 4px; }
  .footer-web { left: 322px; top: 1019px; font-size: 14.5px; font-weight: 700; color: var(--white); display: flex; align-items: center; gap: 6px; }
</style>
</head>
<body>
  <main class="flyer">
    <!-- header -->
    <div class="abs brand-mark"></div>
    <div class="abs brand-name">Bramble Rail Works</div>
    <div class="abs brand-phone">555-014-2273</div>
    <div class="abs brand-tagline">"Because Good Fences Make Good Neighbors"</div>

    <!-- hero -->
    <section class="abs hero" role="img" aria-label="Brown panel over a faint photo of a white vinyl fence"></section>
    <div class="abs hero-accent"></div>
    <h1 class="abs hero-title">WE BUILD<br>FENCES....</h1>
    <p class="abs hero-sub">And we would love<br>to build your fence too!</p>

    <!-- photos -->
    <div class="abs photo-yard" role="img" aria-label="Photo of a newly installed wooden privacy fence around a grassy back yard with a patio umbrella"></div>
    <div class="abs photo-install" role="img" aria-label="Photo of an installer setting wooden fence rails"></div>
    <div class="abs photo-chainlink" role="img" aria-label="Photo of a chainlink fence along a lawn with a company sign"></div>

    <!-- selling column -->
    <p class="abs sell-lead">SELLING<br>FENCE MATERIALS,</p>
    <h2 class="abs sell-strong">IN ADDITION<br>DOING FENCE<br>INSTALLATIONS.</h2>
    <ul class="abs perks">
      <li><svg width="11" height="11" viewBox="0 0 12 12"><circle cx="6" cy="6" r="5" fill="none" stroke="#3a2a1e" stroke-width="1.3"/><path d="M3.5 6.2l1.8 1.8 3.4-3.6" fill="none" stroke="#3a2a1e" stroke-width="1.4"/></svg>Free Estimates</li>
      <li><svg width="11" height="11" viewBox="0 0 12 12"><circle cx="6" cy="6" r="5" fill="none" stroke="#3a2a1e" stroke-width="1.3"/><path d="M3.5 6.2l1.8 1.8 3.4-3.6" fill="none" stroke="#3a2a1e" stroke-width="1.4"/></svg>Professional Installation</li>
      <li><svg width="11" height="11" viewBox="0 0 12 12"><circle cx="6" cy="6" r="5" fill="none" stroke="#3a2a1e" stroke-width="1.3"/><path d="M3.5 6.2l1.8 1.8 3.4-3.6" fill="none" stroke="#3a2a1e" stroke-width="1.4"/></svg>Concrete in EVERY Post</li>
      <li><svg width="11" height="11" viewBox="0 0 12 12"><circle cx="6" cy="6" r="5" fill="none" stroke="#3a2a1e" stroke-width="1.3"/><path d="M3.5 6.2l1.8 1.8 3.4-3.6" fill="none" stroke="#3a2a1e" stroke-width="1.4"/></svg>HOA Submission Assistance</li>
      <li><svg width="11" height="11" viewBox="0 0 12 12"><circle cx="6" cy="6" r="5" fill="none" stroke="#3a2a1e" stroke-width="1.3"/><path d="M3.5 6.2l1.8 1.8 3.4-3.6" fill="none" stroke="#3a2a1e" stroke-width="1.4"/></svg>Lifetime Workmanship Warranty</li>
      <li><svg width="11" height="11" viewBox="0 0 12 12"><circle cx="6" cy="6" r="5" fill="none" stroke="#3a2a1e" stroke-width="1.3"/><path d="M3.5 6.2l1.8 1.8 3.4-3.6" fill="none" stroke="#3a2a1e" stroke-width="1.4"/></svg>Experienced Installation Teams</li>
      <li><svg width="11" height="11" viewBox="0 0 12 12"><circle cx="6" cy="6" r="5" fill="none" stroke="#3a2a1e" stroke-width="1.3"/><path d="M3.5 6.2l1.8 1.8 3.4-3.6" fill="none" stroke="#3a2a1e" stroke-width="1.4"/></svg>Quality Workmanship &amp; Materials</li>
      <li><svg width="11" height="11" viewBox="0 0 12 12"><circle cx="6" cy="6" r="5" fill="none" stroke="#3a2a1e" stroke-width="1.3"/><path d="M3.5 6.2l1.8 1.8 3.4-3.6" fill="none" stroke="#3a2a1e" stroke-width="1.4"/></svg><span>FREE Gate Adjustments for LIFE<small>*some restrictions apply</small></span></li>
    </ul>
    <p class="abs contact-cta">CONTACT US NOW!!</p>

    <!-- estimates column -->
    <h2 class="abs estimate-title">ESTIMATES<br>ARE ALWAYS<br>FREE</h2>
    <p class="abs estimate-copy">Call, email, or message us online to schedule an in-person estimate. If you know your measurements OR have a lot survey, email or call us for a virtual estimate! Monday -Thurs 9AM - 3PM, Friday 9AM - 1 PM</p>
    <p class="abs estimate-note">Beautiful, professionally Installed fences at affordable prices! Many</p>
    <div class="abs photo-boards" role="img" aria-label="Photo of a wooden board fence with a small company sign"></div>

    <!-- materials -->
    <div class="abs materials"></div>
    <div class="abs materials-tab">MATERIAL<br>TYPES WE OFFER:</div>
    <div class="abs material" style="top:611px">
      <span class="material-icon"><svg width="24" height="24" viewBox="0 0 24 24"><rect x="4" y="6" width="4" height="14" fill="#5b3b22"/><rect x="10" y="4" width="4" height="16" fill="#5b3b22"/><rect x="16" y="6" width="4" height="14" fill="#5b3b22"/></svg></span>
      <span class="material-name">WOOD</span>
    </div>
    <div class="abs material" style="top:671px">
      <span class="material-icon"><svg width="24" height="24" viewBox="0 0 24 24" fill="none" stroke="#5b3b22" stroke-width="2"><rect x="3" y="9" width="10" height="6" rx="3" transform="rotate(-45 8 12)"/><rect x="11" y="9" width="10" height="6" rx="3" transform="rotate(-45 16 12)"/></svg></span>
      <span class="material-name">CHAINLINK</span>
    </div>
    <div class="abs material" style="top:731px">
      <span class="material-icon"><svg width="26" height="24" viewBox="0 0 26 24" fill="none" stroke="#5b3b22" stroke-width="1.8"><path d="M4 21V7l3-3 3 3v14M11 21V7l2-3 2 3v14M16 21V7l3-3 3 3v14M2 11h22M2 17h22"/></svg></span>
      <span class="material-name">VINYL</span>
    </div>
    <div class="abs material" style="top:793px">
      <span class="material-icon"><svg width="24" height="24" viewBox="0 0 24 24" fill="none" stroke="#5b3b22" stroke-width="1.8"><path d="M3 5h18M3 19h18M3 5v14M21 5v14M7 5v14M11 5v14M15 5v14M19 5v14"/></svg></span>
      <span class="material-name">Aluminum</span>
    </div>

    <!-- steps -->
    <h3 class="abs steps-title">STEPS TO A NEW<br>FENCE INSTALLATION</h3>
    <ol class="abs steps">
      <li><b>1</b>GETTING A FREE ESTIMATE</li>
      <li><b>2</b>HOA APPROVALS</li>
      <li><b>3</b>UNDERGROUND UTILITIES</li>
      <li><b>4</b>WARRANTY</li>
    </ol>

    <!-- footer -->
    <svg class="abs footer" viewBox="0 0 806 32" preserveAspectRatio="none">
      <rect x="600" y="22" width="206" height="10" fill="#2a7cc7"/>
      <polygon points="0,0 290,0 306,32 0,32" fill="#ef9230"/>
      <polygon points="286,0 600,0 620,32 306,32" fill="#2a7cc7"/>
    </svg>
    <div class="abs footer-phone"><svg width="14" height="14" viewBox="0 0 24 24"><path d="M6.6 10.8a15.1 15.1 0 0 0 6.6 6.6l2.2-2.2a1 1 0 0 1 1-.25 11.4 11.4 0 0 0 3.6.57 1 1 0 0 1 1 1V20a1 1 0 0 1-1 1A17 17 0 0 1 3 4a1 1 0 0 1 1-1h3.5a1 1 0 0 1 1 1c0 1.25.2 2.45.57 3.6a1 1 0 0 1-.25 1z" fill="#fff"/></svg>555-014-2273</div>
    <div class="abs footer-web"><svg width="14" height="14" viewBox="0 0 24 24" fill="none" stroke="#fff" stroke-width="2"><circle cx="12" cy="12" r="10"/><path d="M2 12h20M12 2c3 3 3 17 0 20M12 2c-3 3-3 17 0 20"/></svg>www.bramblerailworks.com</div>
  </main>
</body>
</html>
```